Stationery Design Project

Please create a Stationery Design for Tessory International.
The logo is attached to this brief as part of a business card design.
The company's new name is Tessory International.
Thanks.
Kind regards,
Dale
Dear 4 Designers,
I have changed the name of my company and the design of the logo.
For each of the four of you who took the time to submit proposals prior to my writing this email, I will pay each of you 100USD for your trouble, and I will send you the new design. The only people who are eligible for this 100USD payment will be those four who already have submitted a proposal.
I hope that you consider my approach fair.
Kind regards,
Dale Tessory

```html
<!DOCTYPE html>
<html lang="en">
<head>
<meta charset="utf-8">
<title>Tessory International – Business Card</title>
<link rel="stylesheet" href="https://fonts.googleapis.com/css2?family=Montserrat:wght@700&family=Questrial&display=swap">
<style>
  :root {
    --brand-blue: #0f4f6e;
    --brand-blue-deep: #0b4260;
    --ink-dark: #2a2a2c;
    --text-grey: #4a4a4c;
    --rule-grey: #c9c9c9;
    --paper: #fbfbfa;
    --backdrop: #e7e9eb;
  }
  * { box-sizing: border-box; margin: 0; padding: 0; }
  html, body { width: 1200px; height: 800px; overflow: hidden; }
  body {
    background: var(--backdrop);
    font-family: "Questrial", "Century Gothic", sans-serif;
  }
  .stage {
    position: relative;
    width: 1200px;
    height: 800px;
  }
  .card {
    position: absolute;
    top: 240px;
    width: 540px;
    height: 310px;
    overflow: hidden;
    box-shadow: 0 10px 28px rgba(0,0,0,0.18);
  }
  .card--front { left: 40px; background: var(--paper); }
  .card--back  { left: 620px; background: var(--brand-blue); }

  .wordmark {
    position: absolute;
    left: 36px;
    top: 34px;
    display: flex;
    align-items: center;
    gap: 12px;
    font-size: 26px;
    letter-spacing: 0.5px;
    color: var(--brand-blue);
    text-transform: uppercase;
  }
  .wordmark__square {
    width: 22px;
    height: 22px;
    background: var(--ink-dark);
  }

  .holder {
    position: absolute;
    left: 40px;
    top: 138px;
  }
  .holder__name {
    font-family: "Montserrat", "Century Gothic", sans-serif;
    font-weight: 700;
    font-size: 19px;
    letter-spacing: 0.8px;
    color: var(--brand-blue);
    text-transform: uppercase;
  }
  .holder__title {
    margin-top: 3px;
    font-size: 16px;
    color: var(--text-grey);
  }

  .contacts {
    position: absolute;
    left: 40px;
    right: 24px;
    top: 200px;
    display: flex;
    align-items: flex-start;
    font-size: 13px;
    color: var(--text-grey);
  }
  .contacts__group {
    display: flex;
    flex-direction: column;
    gap: 5px;
    padding: 0 18px;
    border-left: 1px solid var(--rule-grey);
  }
  .contacts__group:first-child { padding-left: 0; border-left: none; }
  .contacts__line { display: flex; align-items: center; gap: 7px; white-space: nowrap; }
  .contacts__icon { width: 13px; height: 13px; flex: none; }

  .accent-band {
    position: absolute;
    left: 0;
    bottom: 0;
    width: 540px;
    height: 60px;
  }

  .back-wordmark {
    position: absolute;
    inset: 0;
    display: flex;
    align-items: center;
    justify-content: center;
    gap: 14px;
    font-size: 30px;
    letter-spacing: 0.8px;
    color: #ffffff;
    text-transform: uppercase;
  }
  .back-wordmark__square {
    width: 24px;
    height: 24px;
    background: #ffffff;
  }
</style>
</head>
<body>
<main class="stage">

  <section class="card card--front" aria-label="Business card front">
    <div class="wordmark">
      <span class="wordmark__square"></span>
      <span class="wordmark__name">Tessory International</span>
    </div>

    <div class="holder">
      <p class="holder__name">Jordan Pell</p>
      <p class="holder__title">General Manager</p>
    </div>

    <div class="contacts">
      <div class="contacts__group">
        <span class="contacts__line">
          <svg class="contacts__icon" viewBox="0 0 14 14" aria-hidden="true">
            <rect width="14" height="14" rx="2" fill="var(--brand-blue)"/>
            <rect x="4" y="2.5" width="6" height="9" rx="1" fill="none" stroke="#fff" stroke-width="1.2"/>
          </svg>
          (07) 5550 2081
        </span>
        <span class="contacts__line">
          <svg class="contacts__icon" viewBox="0 0 14 14" aria-hidden="true">
            <rect width="14" height="14" rx="2" fill="var(--brand-blue)"/>
            <rect x="4" y="2.5" width="6" height="3" fill="#fff"/>
            <rect x="2.5" y="6" width="9" height="5" fill="#fff"/>
          </svg>
          (07) 5550 0381
        </span>
      </div>
      <div class="contacts__group">
        <span class="contacts__line">
          <svg class="contacts__icon" viewBox="0 0 14 14" aria-hidden="true">
            <rect width="14" height="14" rx="2" fill="var(--brand-blue)"/>
            <rect x="2.5" y="4" width="9" height="6" fill="#fff"/>
            <path d="M2.5 4 L7 7.5 L11.5 4" fill="none" stroke="var(--brand-blue)" stroke-width="1"/>
          </svg>
          info@tessory.com
        </span>
        <span class="contacts__line">
          <svg class="contacts__icon" viewBox="0 0 14 14" aria-hidden="true">
            <rect width="14" height="14" rx="2" fill="var(--brand-blue)"/>
            <circle cx="7" cy="7" r="4.2" fill="none" stroke="#fff" stroke-width="1"/>
            <ellipse cx="7" cy="7" rx="1.8" ry="4.2" fill="none" stroke="#fff" stroke-width="0.9"/>
            <line x1="2.8" y1="7" x2="11.2" y2="7" stroke="#fff" stroke-width="0.9"/>
          </svg>
          www.tessory.com
        </span>
      </div>
      <div class="contacts__group">
        <span class="contacts__line">Suite 4, 27B Carrow Street</span>
        <span class="contacts__line">Brightwater QLD 4390</span>
      </div>
    </div>

    <svg class="accent-band" viewBox="0 0 540 60" preserveAspectRatio="none" aria-hidden="true">
      <polygon points="0,44 392,30 420,60 0,60" fill="var(--brand-blue)"/>
      <polygon points="404,30 540,22 540,60 434,60" fill="var(--ink-dark)"/>
    </svg>
  </section>

  <section class="card card--back" aria-label="Business card back">
    <div class="back-wordmark">
      <span class="back-wordmark__square"></span>
      <span class="back-wordmark__name">Tessory International</span>
    </div>
  </section>

</main>
</body>
</html>
```